Updating Business Cards/Stationary
Birchfield Construction Company
Updating Business Cards/Stationary - Construction
Creative Brief
Use specific fonts
Simlar to previous card
Professional
Delvin Kerrow
President
48215 512th St. Ardley, IL 60927
tkerrow@vellmark.net
Wanting to stay similar to previous card - no "harlow" logo, instead replacing it with IL ERB logo. Same address, phone, office/fax, email, website. Wanting to add our " IL-ERB Ren #: QRV-H672041-4" underneath our roofing license #
Same card only using different info. Keeps my jobsite foreman from having info out without my contact info on there as well. Name: Ted Gallway title: project mgt. same address cell: 217/836-2079 email: tedsbuilders48@quillbox.com website/license #s the same.
tkerrow tkerrow
It is on here on the creative brief...
I apologize for the delay - I've emailed it to Ray at Plinth who was going to upload...I will get it on here ASAP...
Quorvo Quorvo
Sir, Can you please upload your previous business card. Thanks

```html
<!DOCTYPE html>
<html lang="en">
<head>
<meta charset="utf-8">
<title>Birchfield Construction Company — Stationery</title>
<link href="https://fonts.googleapis.com/css2?family=Cinzel:wght@700&family=Open+Sans:wght@400;600;700&display=swap" rel="stylesheet">
<style>
  :root {
    --red: #c9353b;
    --red-soft: #f6e3e4;
    --ink: #3a3a3c;
    --muted: #8a8b8e;
    --paper: #ffffff;
    --backdrop: #eceeef;
  }
  * { box-sizing: border-box; margin: 0; padding: 0; }
  html, body { width: 1200px; height: 936px; overflow: hidden; }
  body { background: var(--backdrop); font-family: "Open Sans", sans-serif; color: var(--ink); }
  .canvas { position: relative; width: 1200px; height: 936px; }
  .sheet { position: absolute; background: var(--paper); box-shadow: 0 2px 6px rgba(0,0,0,.12); overflow: hidden; }

  .brand { display: flex; align-items: center; gap: 8px; font-family: "Cinzel", serif; font-weight: 700; color: var(--ink); line-height: 1.05; }
  .brand-mark { width: 12px; height: 12px; background: var(--red); flex: none; }
  .brand-name { text-transform: uppercase; letter-spacing: .5px; }

  .band { position: absolute; left: 0; right: 0; background: var(--red); color: #fff; display: flex; align-items: center; justify-content: center; font-weight: 600; letter-spacing: 4px; text-transform: lowercase; }

  /* Letterhead */
  .letterhead { left: 147px; top: 20px; width: 416px; height: 584px; }
  .letterhead .brand { position: absolute; left: 40px; top: 50px; font-size: 12px; }
  .letterhead .brand-name { width: 150px; }
  .letterhead .sender { position: absolute; right: 28px; top: 48px; font-size: 5.5px; color: var(--muted); text-align: right; line-height: 1.6; }
  .letter { position: absolute; left: 40px; top: 150px; width: 320px; font-size: 5.5px; line-height: 1.7; color: var(--muted); }
  .letter p { margin-bottom: 9px; }
  .signature { width: 40px; height: 14px; background: linear-gradient(90deg, #bdbdbd, #e2e2e2); margin: 4px 0 8px; border-radius: 3px; }
  .letter .signer { color: var(--ink); font-weight: 600; }
  .letterhead .band { bottom: 26px; height: 6px; }

  /* Folder */
  .folder { left: 589px; top: 20px; width: 507px; height: 602px; }
  .folder .brand { position: absolute; left: 0; right: 0; top: 258px; justify-content: center; font-size: 30px; gap: 14px; }
  .folder .brand-mark { width: 26px; height: 26px; }
  .folder .brand-name { text-align: center; width: 300px; }
  .folder .band { bottom: 18px; height: 14px; font-size: 6.5px; }

  /* Business cards */
  .card { left: 51px; width: 203px; height: 114px; }
  .card-front { top: 665px; }
  .card-front .brand { position: absolute; left: 10px; top: 14px; font-size: 8px; gap: 5px; }
  .card-front .brand-mark { width: 8px; height: 8px; }
  .card-front .brand-name { width: 90px; }
  .badge { position: absolute; left: 112px; top: 14px; width: 18px; height: 18px; border-radius: 50%; background: var(--red); }
  .card-details { position: absolute; left: 136px; top: 12px; font-size: 4.2px; line-height: 1.55; color: var(--muted); }
  .card-details .who { color: var(--ink); font-weight: 700; font-size: 5px; }
  .card-front .licenses { position: absolute; left: 10px; bottom: 16px; font-size: 4.2px; line-height: 1.55; color: var(--muted); }
  .card .band { bottom: 5px; height: 5px; }
  .card-back { top: 792px; }
  .card-back .brand { position: absolute; left: 10px; top: 16px; font-size: 8px; gap: 5px; }
  .card-back .brand-mark { width: 8px; height: 8px; }
  .card-back .brand-name { width: 90px; }
  .card-back .card-details { left: 128px; top: 16px; }

  /* Envelopes */
  .envelope-front { left: 264px; top: 665px; width: 388px; height: 228px; }
  .envelope-front .brand { position: absolute; left: 34px; top: 30px; font-size: 12px; }
  .envelope-front .brand-name { width: 150px; }
  .envelope-front .band { bottom: 52px; height: 12px; font-size: 6px; justify-content: flex-start; padding-left: 34px; }
  .envelope-back { left: 665px; top: 665px; width: 431px; height: 228px; }
  .envelope-back svg { position: absolute; inset: 0; }
  .envelope-back .site { position: absolute; left: 0; right: 0; top: 74px; text-align: center; color: #fff; font-size: 9px; letter-spacing: 3px; font-weight: 600; }
</style>
</head>
<body>
<main class="canvas">

  <section class="sheet letterhead" aria-label="Letterhead">
    <div class="brand"><span class="brand-mark"></span><span class="brand-name">Birchfield Construction Company</span></div>
    <address class="sender">48215 512th St. Ardley, IL 60927<br>217/836-2079<br>tkerrow@vellmark.net</address>
    <div class="letter">
      <p>July 4, 2017<br>Dear Sir,<br>420 Cedar Lane, Ardley, IL</p>
      <p>Thank you for choosing our team for your upcoming building project. We have reviewed the plans you shared and prepared a full estimate covering materials, labor and scheduling for each phase of the work.</p>
      <p>Our crew will begin site preparation once permits are approved. All roofing and framing will follow current state codes and our own safety standards.</p>
      <p>Please review the enclosed documents and contact our office with any questions. We look forward to working with you and delivering a home built to last for many years.</p>
      <p>Best Regards,</p>
      <div class="signature" role="img" aria-label="Handwritten signature"></div>
      <p><span class="signer">Delvin Kerrow</span><br>President</p>
    </div>
    <div class="band"></div>
  </section>

  <section class="sheet folder" aria-label="Presentation folder">
    <div class="brand"><span class="brand-mark"></span><span class="brand-name">Birchfield Construction Company</span></div>
    <div class="band">www.birchfieldconstructioncompany.com</div>
  </section>

  <section class="sheet card card-front" aria-label="Business card, president">
    <div class="brand"><span class="brand-mark"></span><span class="brand-name">Birchfield Construction Company</span></div>
    <span class="badge" aria-hidden="true"></span>
    <div class="card-details">
      <div class="who">Delvin Kerrow</div>
      President<br>48215 512th St.<br>Ardley, IL 60927<br>Cell: 217/836-2079<br>tkerrow@vellmark.net
    </div>
    <div class="licenses">Roofing Lic #: 104.018822<br>IL-ERB Ren #: QRV-H672041-4</div>
    <div class="band"></div>
  </section>

  <section class="sheet card card-back" aria-label="Business card, project management">
    <div class="brand"><span class="brand-mark"></span><span class="brand-name">Birchfield Construction Company</span></div>
    <div class="card-details">
      <div class="who">Ted Gallway</div>
      Project Mgt.<br>Cell: 217/836-2079<br>tedsbuilders48@quillbox.com
    </div>
    <div class="band"></div>
  </section>

  <section class="sheet envelope-front" aria-label="Envelope front">
    <div class="brand"><span class="brand-mark"></span><span class="brand-name">Birchfield Construction Company</span></div>
    <div class="band">www.birchfieldconstructioncompany.com</div>
  </section>

  <section class="sheet envelope-back" aria-label="Envelope back">
    <svg width="431" height="228" viewBox="0 0 431 228" aria-hidden="true">
      <polygon points="0,0 431,0 431,60 215.5,128 0,60" fill="var(--red)"/>
      <polyline points="0,228 215.5,128 431,228" fill="none" stroke="#e4e4e4" stroke-width="1"/>
    </svg>
    <div class="site">www.urwebsitename.com</div>
  </section>

</main>
</body>
</html>
```